Recipe mobile app, new flow and design for uploading recipe process

I need a new recipe upload process that's simple, intuitive, and engaging.
The goal is to have a user-friendly and fast flow.
The app is a social recipe library where anyone can upload a recipe after signing up. I currently have a flow, but it's "boring," so I'd like to significantly improve this aspect of the app.
When I create a new recipe, it's immediately saved and labeled as a draft. I'll then need to specify:
- Recipe title
- Cover image (required)
- Number of people (how many people is the recipe for)
- Ingredients (name, quantity, and unit of measurement)
- Recipe explanation (broken down into steps, and I can optionally attach an image to each step)
- Upload
Every change is immediately saved, so you can edit, exit, and resume editing later.
I've attached images of the app and the current upload process.
Thank you.
Low design quality
Good morning everyone,
some of the designs received are fantastic, but please make sure to carefully read the requirement so as not to do extra work.
The requirement is to redesign the flow that a user follows when uploading a recipe to the platform.
We have uploaded the current app screens to give you an idea of what the product looks like, what the colors and style are, but we don’t need a full redesign - only the part mentioned above, while keeping the existing style and colors (we cannot rework the entire theme).
To clarify: if you look at the screens shared in the zip file attached to the project, the focus should be on the screens from 5_.png to 10_.png.
These screens can be redesigned in the most creative way you think, as long as the overall theme remains unchanged.
Thank you for your attention.

```html
<!DOCTYPE html>
<html lang="en">
<head>
<meta charset="utf-8">
<title>Recipe Upload Flow</title>
<link rel="stylesheet" href="https://fonts.googleapis.com/css2?family=Ubuntu:wght@400;500;700&display=swap">
<style>
:root{
  --backdrop:#8d8d8d;
  --screen:#f6f6f6;
  --green:#23a35c;
  --orange:#fb7d3d;
  --mint:#dcf6e8;
  --ink:#1d1d1d;
  --line:#cfcfcf;
  --field:#f1f1f1;
}
*{box-sizing:border-box;margin:0;padding:0}
html,body{width:857px;height:1200px;overflow:hidden}
body{background:radial-gradient(ellipse at center,#9a9a9a 0%,var(--backdrop) 60%,#7a7a7a 100%);font-family:"Ubuntu",sans-serif;color:var(--ink);position:relative}
.screen{position:absolute;width:235px;background:var(--screen);overflow:hidden}
.row-top{top:79px;height:453px}
.row-bottom{top:557px;height:563px}
.col-1{left:60px}.col-2{left:312px}.col-3{left:563px}
.back{position:absolute;left:34px;top:19px;width:14px;height:14px}
.btn{position:absolute;top:15px;height:22px;border-radius:11px;background:var(--green);color:#fff;font-size:9px;font-weight:700;display:flex;align-items:center;justify-content:center;letter-spacing:.3px}
.btn-next{left:158px;width:48px}
.btn-upload{left:124px;width:93px}
.title{position:absolute;left:58px;top:17px;font-size:15px;font-weight:700;letter-spacing:.5px}
.input{position:absolute;left:20px;top:69px;width:195px;height:28px;border:1px solid var(--line);border-radius:14px;background:var(--field);font-size:9px;padding-left:20px;display:flex;align-items:center}
.photo{position:absolute;left:15px;top:115px;width:204px;height:309px;border-radius:8px}
.photo-dim{background:linear-gradient(180deg,#4a3426 0%,#7a5a38 35%,#b89a6a 55%,#8a6a48 80%,#4a3628 100%)}
.photo-bright{background:linear-gradient(160deg,#e9e6e1 0%,#c7845a 30%,#efe2c8 55%,#5a3a2a 75%,#f2f0ee 100%)}
.choose{position:absolute;left:0;right:0;top:130px;text-align:center;color:#fff;font-size:11.5px;font-weight:500}
.choose .cam{width:32px;height:32px;border-radius:50%;background:var(--orange);margin:0 auto 8px;display:flex;align-items:center;justify-content:center}
.home{position:absolute;left:58px;width:118px;height:2px;background:#bdbdbd;border-radius:1px}
.fab{position:absolute;width:32px;height:32px;border-radius:50%;background:var(--orange);color:#fff;display:flex;align-items:center;justify-content:center;box-shadow:0 2px 5px rgba(0,0,0,.18);z-index:3}
.persons{position:absolute;left:18px;top:74px;width:200px;height:63px;background:var(--mint);border-radius:9px;box-shadow:1px 3px 4px rgba(0,0,0,.15);font-size:10.5px;line-height:17px;padding:13px 0 0 13px}
.persons p{width:128px}
.pill{position:absolute;left:153px;top:18px;width:32px;height:15px;border:1px solid #bbb;border-radius:8px;background:#fff;font-size:7px;color:#555;display:flex;align-items:center;justify-content:center}
.divider{position:absolute;left:5px;top:151px;width:227px;height:1px;background:#d0d0d0}
.ingredient{position:absolute;left:17px;width:200px;height:67px;background:#fff;border-radius:11px;box-shadow:0 2px 4px rgba(0,0,0,.14)}
.ingredient .name{position:absolute;left:11px;top:9px;width:178px;height:28px;background:var(--field);border:1px solid var(--line);border-radius:3px;font-size:11px;padding-left:19px;display:flex;align-items:center}
.ingredient .qty{position:absolute;left:12px;top:43px;width:44px;height:17px;border:1px solid var(--line);border-radius:9px;font-size:8.5px;color:#666;display:flex;align-items:center;justify-content:center}
.ingredient .unit{position:absolute;left:68px;top:46px;font-size:9px;font-weight:500}
.ingredient .rule{position:absolute;top:54px;width:34px;height:1px;background:#999;right:43px}
.ingredient .caret{position:absolute;left:162px;top:50px;width:0;height:0;border-left:3.5px solid transparent;border-right:3.5px solid transparent;border-top:4px solid #333}
.steps-card{position:absolute;left:9px;top:69px;width:216px;height:457px;background:#fff;border:1px solid #ddd;border-radius:3px}
.step-img{position:absolute;width:74px;height:74px;border-radius:50%;border:3px solid var(--orange);padding:3px;background:#fff}
.step-img.green{border-color:var(--green)}
.step-img span{display:block;width:100%;height:100%;border-radius:50%}
.badge{position:absolute;width:22px;height:22px;border-radius:50%;background:var(--orange);color:#fff;font-size:9px;font-weight:700;display:flex;align-items:center;justify-content:center;border:1.5px solid #fff;z-index:2}
.badge.green{background:var(--green)}
.step-text{position:absolute;font-size:9.5px;line-height:17px;font-weight:500}
</style>
</head>
<body>

<!-- Screen: recipe name + cover -->
<section class="screen row-top col-1">
  <svg class="back" viewBox="0 0 14 14"><path d="M9 2 4 7l5 5" fill="none" stroke="#222" stroke-width="1.5"/></svg>
  <div class="btn btn-next">NEXT</div>
  <div class="input">Recipe Name</div>
  <div class="photo photo-dim" role="img" aria-label="Dimmed photo of a slice of layered cream dessert with a mint sprig">
    <div class="choose">
      <div class="cam"><svg width="13" height="11" viewBox="0 0 13 11"><path d="M1 3h2.5l1-2h4l1 2H12v7H1z" fill="#fff"/><circle cx="6.5" cy="6.3" r="2" fill="var(--orange)"/></svg></div>
      Choose Photo
    </div>
  </div>
  <div class="home" style="top:439px"></div>
</section>

<!-- Screen: filled name + cover -->
<section class="screen row-top col-2">
  <svg class="back" viewBox="0 0 14 14"><path d="M9 2 4 7l5 5" fill="none" stroke="#222" stroke-width="1.5"/></svg>
  <div class="btn btn-next">NEXT</div>
  <div class="input">Tiramisu</div>
  <div class="photo photo-bright" role="img" aria-label="Photo of a tiramisu slice topped with a strawberry on a white plate with chocolate sauce"></div>
  <div class="home" style="top:439px"></div>
</section>

<!-- Screen: ingredients empty -->
<section class="screen row-top col-3">
  <svg class="back" viewBox="0 0 14 14"><path d="M9 2 4 7l5 5" fill="none" stroke="#222" stroke-width="1.5"/></svg>
  <div class="title">INGREDIENTS</div>
  <div class="btn btn-next">NEXT</div>
  <div class="persons"><p>For how many persons is this recipe?</p><div class="pill">EX:4</div></div>
  <div class="fab" style="left:176px;top:387px"><svg width="12" height="12"><path d="M6 1v10M1 6h10" stroke="#fff" stroke-width="2"/></svg></div>
  <div class="home" style="top:439px"></div>
</section>

<!-- Screen: ingredients list -->
<section class="screen row-bottom col-1">
  <svg class="back" viewBox="0 0 14 14"><path d="M9 2 4 7l5 5" fill="none" stroke="#222" stroke-width="1.5"/></svg>
  <div class="title">INGREDIENTS</div>
  <div class="btn btn-next">NEXT</div>
  <div class="persons"><p>For how many persons is this recipe?</p><div class="pill">EX:4</div></div>
  <div class="divider"></div>
  <div class="ingredient" style="top:167px"><div class="name">Milk</div><div class="qty">250.0</div><div class="unit">Millimeters</div><div class="rule"></div><div class="caret"></div></div>
  <div class="ingredient" style="top:241px"><div class="name">Sugar</div><div class="qty">0.0</div><div class="unit">As Needed</div><div class="rule"></div><div class="caret"></div></div>
  <div class="ingredient" style="top:314px"><div class="name">Chocolate</div><div class="qty">10.0</div><div class="unit">Grams</div><div class="rule" style="width:50px"></div><div class="caret"></div></div>
  <div class="ingredient" style="top:388px"><div class="name">Eggs</div><div class="qty">250.0</div><div class="unit">Pieces</div><div class="rule" style="width:50px"></div><div class="caret"></div></div>
  <div class="ingredient" style="top:461px"><div class="name">Water</div><div class="qty">500.0</div><div class="unit">Millimeters</div><div class="rule" style="width:32px"></div><div class="caret"></div></div>
  <div class="fab" style="left:186px;top:447px"><svg width="12" height="12"><path d="M6 1v10M1 6h10" stroke="#fff" stroke-width="2"/></svg></div>
  <div class="home" style="top:548px"></div>
</section>

<!-- Screen: steps empty -->
<section class="screen row-bottom col-2">
  <svg class="back" viewBox="0 0 14 14"><path d="M9 2 4 7l5 5" fill="none" stroke="#222" stroke-width="1.5"/></svg>
  <div class="title">STEPS</div>
  <div class="btn btn-upload">UPLOAD RECIPE</div>
  <div class="home" style="top:548px"></div>
</section>

<!-- Screen: steps list -->
<section class="screen row-bottom col-3">
  <svg class="back" viewBox="0 0 14 14"><path d="M9 2 4 7l5 5" fill="none" stroke="#222" stroke-width="1.5"/></svg>
  <div class="title">STEPS</div>
  <div class="btn btn-upload">UPLOAD RECIPE</div>
  <div class="steps-card">
    <div class="badge" style="left:24px;top:31px">01</div>
    <div class="step-img" style="left:22px;top:31px"><span role="img" aria-label="Photo of egg yolks in a glass bowl" style="background:radial-gradient(circle at 55% 65%,#f4b13a 0%,#f7d9a8 30%,#d9d6d2 70%,#a9a5a0 100%)"></span></div>
    <div class="step-text" style="left:113px;top:41px">Careful to keep<br>The whites totally<br>Free of yolk</div>

    <div class="badge green" style="left:125px;top:136px">02</div>
    <div class="step-img green" style="left:123px;top:137px"><span role="img" aria-label="Photo of whites being beaten in a bowl" style="background:radial-gradient(circle at 60% 65%,#f2b43c 0%,#c7bfb3 40%,#4a4a4a 100%)"></span></div>
    <div class="step-text" style="left:19px;top:147px">Beat the whites<br>&amp; add it to the bowl<br>with the mascarpone</div>

    <div class="badge" style="left:24px;top:243px">03</div>
    <div class="step-img" style="left:22px;top:244px"><span role="img" aria-label="Photo of whipped mascarpone cream" style="background:radial-gradient(circle at 45% 50%,#fbf3c6 0%,#efe3a4 50%,#b9b08a 100%)"></span></div>
    <div class="step-text" style="left:113px;top:253px">Prinkle over the<br>Unsweetened<br>Cocoa powder</div>

    <div class="badge green" style="left:125px;top:349px">04</div>
    <div class="step-img green" style="left:123px;top:350px"><span role="img" aria-label="Photo of smooth yellow cream in a glass bowl" style="background:radial-gradient(circle at 50% 50%,#f7d66a 0%,#e9b938 60%,#8a7a50 100%)"></span></div>
    <div class="step-text" style="left:19px;top:369px">The mascarpone<br>Cream is ready</div>
  </div>
  <div class="fab" style="left:185px;top:507px"><svg width="12" height="12"><path d="M6 1v10M1 6h10" stroke="#fff" stroke-width="2"/></svg></div>
  <div class="home" style="top:548px"></div>
</section>

</body>
</html>
```